Business Card Design

We are a residential half way house for the addict ,the alcoholic and dual diagnosed in recovery.
i house both men and woman age 18+

Industry/Entity Type

Residential

```html
<!DOCTYPE html>
<html lang="en">
<head>
<meta charset="utf-8">
<title>Harbor Light Family Sober House – Business Card</title>
<link rel="stylesheet" href="https://fonts.googleapis.com/css2?family=Didact+Gothic&family=Montserrat:wght@700&display=swap">
<style>
  :root {
    --page-bg: #ffffff;
    --card-bg: #ffffff;
    --brand-green: #43973a;
    --brand-orange: #f0861f;
    --ink-dark: #2b2b2b;
    --ink-mid: #3a3a3a;
    --ink-light: #ffffff;
  }
  * { margin: 0; padding: 0; box-sizing: border-box; }
  html, body {
    width: 1200px;
    height: 850px;
    overflow: hidden;
    background: var(--page-bg);
  }
  .canvas {
    position: relative;
    width: 1200px;
    height: 850px;
  }
  .card {
    position: absolute;
    left: 130px;
    top: 160px;
    width: 940px;
    height: 530px;
    border-radius: 30px;
    overflow: hidden;
    background: var(--card-bg);
    border: 1px solid #e6e6e6;
  }
  .card-wave {
    position: absolute;
    inset: 0;
    width: 940px;
    height: 530px;
  }
  .brand {
    position: absolute;
    left: 70px;
    top: 70px;
    width: 320px;
    display: flex;
    flex-direction: column;
    align-items: center;
    gap: 18px;
  }
  .brand-dot {
    width: 78px;
    height: 78px;
    border-radius: 50%;
    background: var(--brand-green);
  }
  .brand-name {
    font-family: "Montserrat", sans-serif;
    font-weight: 700;
    font-size: 24px;
    line-height: 1.25;
    color: var(--ink-dark);
    text-align: center;
  }
  .holder {
    position: absolute;
    right: 110px;
    top: 64px;
    text-align: right;
    color: var(--ink-mid);
  }
  .holder-name {
    font-family: "Montserrat", sans-serif;
    font-weight: 700;
    font-size: 29px;
    color: var(--ink-dark);
    line-height: 1.2;
  }
  .holder-role,
  .holder-note {
    font-family: "Didact Gothic", sans-serif;
    font-size: 27px;
    line-height: 1.2;
  }
  .holder-role { margin-top: 8px; }
  .holder-note { margin-top: 18px; }
  .contacts {
    position: absolute;
    right: 110px;
    top: 262px;
    list-style: none;
    display: flex;
    flex-direction: column;
    align-items: flex-end;
    color: var(--ink-light);
    font-family: "Didact Gothic", sans-serif;
    font-size: 30px;
    line-height: 1;
  }
  .contact-row {
    display: flex;
    align-items: flex-start;
    gap: 10px;
    margin-bottom: 12px;
  }
  .contact-row .icon {
    width: 28px;
    height: 28px;
    flex: none;
    fill: var(--ink-light);
  }
  .phone-lines {
    display: flex;
    flex-direction: column;
    gap: 12px;
  }
</style>
</head>
<body>
<div class="canvas">
  <div class="card">
    <svg class="card-wave" viewBox="0 0 940 530" aria-hidden="true">
      <path fill="var(--brand-orange)" d="M0 326 C180 372 330 352 480 290 S800 196 940 194 L940 210 C800 212 620 252 480 300 S180 384 0 350 Z"/>
      <path fill="var(--brand-green)" d="M0 362 C190 406 330 372 490 310 S810 222 940 220 L940 530 L0 530 Z"/>
    </svg>

    <div class="brand">
      <span class="brand-dot"></span>
      <p class="brand-name">Harbor Light<br>Family Sober House Inc.</p>
    </div>

    <div class="holder">
      <p class="holder-name">Marisa Delgado</p>
      <p class="holder-role">Owner</p>
      <p class="holder-note">(15 yrs.in recovery)</p>
    </div>

    <ul class="contacts">
      <li class="contact-row">
        <svg class="icon" viewBox="0 0 24 24" aria-label="Phone"><path d="M6.6 2.5c.6-.3 1.3 0 1.6.6l1.6 3.6c.2.5.1 1.1-.3 1.4L8 9.3c.9 2.4 2.6 4.4 4.9 5.7l1.3-1.4c.4-.4 1-.5 1.5-.2l3.5 1.8c.6.3.8 1 .6 1.6l-.9 2.5c-.3.8-1.1 1.3-2 1.2C9.3 19.8 3.5 12.8 4.1 5.4c.1-.8.6-1.5 1.3-1.8z"/></svg>
        <span class="phone-lines"><span>(555) 014-0305</span><span>(555) 014-0306</span></span>
      </li>
      <li class="contact-row">
        <svg class="icon" viewBox="0 0 24 24" aria-label="Fax"><path d="M7 2h8l2 2v5H7z M3 10h18v10H3z"/><rect x="6" y="12" width="4" height="2" fill="var(--brand-green)"/><rect x="6" y="16" width="12" height="2" fill="var(--brand-green)"/></svg>
        <span>(555) 019-5536</span>
      </li>
      <li class="contact-row">
        <svg class="icon" viewBox="0 0 24 24" aria-label="Email"><path d="M2 5h20v14H2z M4 7v.4l8 6 8-6V7z M4 9.9V17h16V9.9l-8 6z" fill-rule="evenodd"/></svg>
        <span>marisadelgado@mailbox.com</span>
      </li>
      <li class="contact-row">
        <svg class="icon" viewBox="0 0 24 24" aria-label="Address"><path d="M12 2 1 10h3v11h16V10h3z M7 13h4v6H7z M13 13h4v4h-4z" fill-rule="evenodd"/></svg>
        <span>1820 Palm Grove Rd. Lake Haven,Fla 33400</span>
      </li>
    </ul>
  </div>
</div>
</body>
</html>
```